Buch-/E-Book-Cover
Zielgruppe
Als Manufaktur einzigartiger Fachmedien präsentiert verlag-momentum Schlüsseltechnologien und ihre Märkte. Faszination für Technik ist die Grundlage unserer Arbeit. Mehr als 25 Jahre verlegerische Erfahrung und das Verständnis für Technologiemärkte machen uns zu einem anerkannten Partner der Industrie.
Unsere Medienmarken knüpfen ein starkes und weit verzweigtes Netzwerk – Print und digital – , in dem sich Anbieter und Anwender von Technologien und Produkten in ihren Zielsetzungen wiederfinden.
Unsere Magazine, Events und Netzwerkveranstaltungen sowie kundenspezifische Kommunikations- & Strategiekampagnen setzen in ihren Zielmärkten Maßstäbe und genießen bei Lesern, Kunden und Partnern Vertrauen und Respekt.
Für das ausgeschriebene Projekt handelt es sich um unsere Jahrespublikation MACHINA.ahead ULUWANO.
ULUWANO {polynesisch: Freiraum}
Das Jahrbuch der Industrie. Für Vorwärtsdenker und Zukunftsmacher.
Wandel bestimmt unsere Zeit und verändert unsere Gesellschaft, unsere Unternehmen, uns alle.
Im Wandel liegt Freiraum zur Gestaltung. Gesellschaftlicher Wandel, Technologie-Wandel, Klimawandel, Wertewandel, Führungswandel oder Organisationswandel sind nur einige Beispiele. Wer dabei den Wandel in engen Bahnen denkt, verschenkt Potential. Veränderung braucht Freiraum für neue Ideen und Perspektiven sowie Persönlichkeiten, die diesen nutzen wollen.
Aber wer gestaltet die Zukunft der Industrie und ihrer Branchen? Und wie?
Wir geben 75 Personen aus der Industrie den Freiraum, ihre Perspektiven auf und aus dem Wandel zu erzählen. Warum? Weil sie uns begeistert haben, in persönlichen Treffen und Gesprächen, durch streitbare Meinungen und ehrliche Geschichten. Weil sie die Zukunft verändern.
ULUWANO ist eine Aufforderung: Zum Mitdenken, Weiterdenken, aber auch Nachdenken.
ULUWANO – BÜHNE FÜR EINFÄLLE
Ein Referenzbuch, das den Namen verdient: unkonven..
Aufgabenstellung
1. Kurzzusammenfassung der Ausschreibung
Die 2. Ausgabe des Jahrbuchs der Industrie, MACHINA.ahead ULUWANO 2022, erscheint im Oktober 2022. Für das Cover sucht der verlag-momentum Verlag neue Vorschläge, die die Themen Freiraum und Wandel in den Fokus stellen und einen optischen Bezug zu der Erstausgabe 2021 setzen.
Die Anforderungen an die Illustration finden Sie untenstehend. Das Marketingteam von verlag-momentum wird drei Illustrationen auswählen und im Anschluss die Kontaktel Community von MACHINA.ahead abstimmen lassen, welches das Sieger-Cover wird. Zusätzlich wird es einen Folgeauftrag für die Gestaltung des Versandkartons geben.
2. Gestalterische & Inhaltliche Anforderungen
• Format: 195x250 mm + Anschnitt
• Rücken: ca. 2 cm (Stand letzte Publikation 2021)
• Auflösung: Druckqualität, mind. 300 dpi
• Inhaltliche Elemente:
- ULUWANO
- {polynesisch: Freiraum}
- Untersatz: Das Jahrbuch der Industrie. Für Vorwärtsdenker und Zukunftsmacher.
- MACHINA.ahead Logo
WICHTIG: Entweder soll der aktuelle Schriftzug ULUWANO oder die Farbe orange (0/80/100/0) (siehe Beispiel ULUWANO 2021) als Wiedererkennung in die Gestaltungen eingebunden werden.

```html
<!DOCTYPE html>
<html lang="de">
<head>
<meta charset="utf-8">
<title>ULUWANO 2022 – Jahrbuch der Industrie, Cover</title>
<link rel="stylesheet" href="https://fonts.googleapis.com/css2?family=Oswald:wght@500;600&family=Roboto+Condensed:ital,wght@0,400;0,500;1,400&display=swap">
<style>
  :root {
    --paper: #ffffff;
    --surface-dark: #1c1b1a;
    --surface-mid: #3a3733;
    --surface-warm: #4a3f2f;
    --title-white: #ffffff;
    --accent-lime: #c6dc2a;
    --logo-pink: #e0147a;
    --note-white: #e9e9e9;
  }
  * { box-sizing: border-box; margin: 0; padding: 0; }
  html, body {
    width: 1200px; height: 720px; overflow: hidden;
    background: var(--paper);
  }
  .stage { position: relative; width: 1200px; height: 720px; }

  /* shared backdrop for spine and front */
  .surface {
    position: absolute; inset: 0;
    background:
      radial-gradient(ellipse 40% 30% at 35% 55%, var(--surface-warm) 0%, transparent 70%),
      radial-gradient(ellipse 60% 45% at 60% 30%, var(--surface-mid) 0%, transparent 75%),
      linear-gradient(160deg, var(--surface-mid) 0%, var(--surface-dark) 60%, #111 100%);
  }

  /* ---------- spine ---------- */
  .spine {
    position: absolute; left: 290px; top: 40px;
    width: 49px; height: 640px; overflow: hidden;
  }
  .spine-tagline {
    position: absolute; top: 48px; right: 6px;
    writing-mode: vertical-rl;
    font: 500 9.5px/1 "Roboto Condensed", sans-serif;
    color: var(--accent-lime); white-space: nowrap;
  }
  .spine-title {
    position: absolute; left: 4px; top: 335px; width: 41px;
    font: 600 24px/0.9 "Oswald", sans-serif;
    color: var(--title-white); text-align: center; letter-spacing: -0.5px;
  }
  .spine-year {
    position: absolute; left: 15px; bottom: 52px;
    writing-mode: vertical-rl; transform: rotate(180deg);
    font: 600 16px/1 "Oswald", sans-serif; color: var(--accent-lime);
  }

  /* ---------- front cover ---------- */
  .front {
    position: absolute; left: 412px; top: 40px;
    width: 498px; height: 640px; overflow: hidden;
  }
  .cover-title {
    position: absolute; right: 6px; top: -14px;
    font: 600 188px/0.86 "Oswald", sans-serif;
    color: var(--title-white); text-align: right; letter-spacing: -4px;
    text-transform: uppercase;
  }
  .cover-title span { display: block; }
  .cover-title .gloss {
    font: italic 400 10px/1 "Roboto Condensed", sans-serif;
    letter-spacing: 0; text-align: right;
    margin: 6px 6px 14px 0; color: var(--note-white);
  }
  .cover-year {
    position: absolute; left: 142px; top: 222px;
    writing-mode: vertical-rl; transform: rotate(180deg);
    font: 600 40px/1 "Oswald", sans-serif; color: var(--accent-lime);
  }
  .cover-subline {
    position: absolute; left: 142px; top: 330px; width: 70px;
    font: 500 12.5px/1.3 "Roboto Condensed", sans-serif; color: var(--accent-lime);
  }
  .publisher-mark {
    position: absolute; left: 142px; top: 568px;
    display: flex; align-items: center; gap: 3px;
  }
  .publisher-mark .dot { width: 6px; height: 6px; background: var(--logo-pink); }
  .publisher-mark .name {
    font: 500 9px/1 "Roboto Condensed", sans-serif; color: var(--logo-pink);
  }
</style>
</head>
<body>
<main class="stage">

  <section class="spine" aria-label="Buchrücken">
    <div class="surface" role="img" aria-label="Dunkle, organisch gelochte Oberfläche mit goldenen Lichtpunkten"></div>
    <p class="spine-tagline">Das Jahrbuch der Industrie. Für Vorwärtsdenker und Zukunftsmacher.</p>
    <h2 class="spine-title">ULU<br>WA<br>NO</h2>
    <p class="spine-year">2022</p>
  </section>

  <section class="front" aria-label="Vorderseite">
    <div class="surface" role="img" aria-label="Dunkle, organisch gelochte Oberfläche mit goldenen Lichtpunkten"></div>
    <h1 class="cover-title">
      <span>ULU</span>
      <span>WA</span>
      <span class="gloss">{polynesisch – Freiraum}</span>
      <span>NO</span>
    </h1>
    <p class="cover-year">2022</p>
    <p class="cover-subline">Das Jahrbuch der Industrie. Für Vorwärts&shy;denker und Zukunfts&shy;macher.</p>
    <div class="publisher-mark">
      <span class="dot"></span>
      <span class="name">MACHINA.ahead</span>
    </div>
  </section>

</main>
</body>
</html>
```